Talvane Companies Business Card Design

We need a new business card for our Private Equity Real Estate Development firm, “Talvane” and our EB-5 regional center “Moorfield Regional Center” on one card. We prefer a design that is simple, elegant, and represents the luxury products we design and build as well as the financial security and stability our successful history has produced. We are an industry leader in our field and 3rd generation family business that has evolved into an institutional quality investment platform. Considered design size is standard business card dimensions (3.5 x 2 inches with an additional 1/8 inch space for design elements or backgrounds that extend beyond the finished size of your piece.

Target Market(s)

• High net worth individuals
• Highly skilled technical workers and physicians in the US seeking investment-based immigration opportunities
• Sophisticated private equity investors
• Intermediary partners include domestic attorneys and investment brokers, as well as international agent networks
• US real estate developers

Industry/Entity Type

Finance

Contact Information for Business Card

(Providing placeholder info for personal information, please design for longer character spaces, longer names and addresses etc..)
• Logo for Talvane
• Logo for Moorfield Regional Center
• Full name: Dorian Talvane
• Job title: CEO
• Email address: dtalvane@talvanecompanies.example
• Cell phone number: +1.555.318.4476
• Office number +1.555.240.6185
• Office address: Quillan Court 5, 4817 Vista Ardell, San Ramon, CA.
• Website: www.talvanecompanies.example

Font styles to use
Serif
Sans Serif

Colors
ec1f27
ffffff
000000

Requirements
Must have
• • Logo for Talvane
• • Logo for Moorfield Regional Center
• - Use rounded corners
• (See .ai file included for logos)
Nice to have
• • Simple, elegant design
• • Aesthetically compatible with our website design (www.talvanecompanies.example)
• • Color palette including but not limited to white, black, and red (as per logos)
Should not have
• - Not too much red color
• - Do not stack both logos on top of each other

```html
<!DOCTYPE html>
<html lang="en">
<head>
<meta charset="utf-8">
<title>Talvane Companies Business Card</title>
<link rel="stylesheet" href="https://fonts.googleapis.com/css2?family=Cinzel:wght@400;600&family=Work+Sans:wght@400;600&display=swap">
<style>
  :root {
    --stage: #d9d9d9;
    --card-dark: #2d2d2e;
    --card-light: #ffffff;
    --ink: #1a1a1a;
    --ink-soft: #555555;
    --silver: #c9c9c9;
    --red: #ec1f27;
    --rule: #222222;
  }
  * { margin: 0; padding: 0; box-sizing: border-box; }
  html, body { width: 1200px; height: 810px; overflow: hidden; background: var(--stage); }
  .canvas {
    width: 1200px; height: 810px;
    display: flex; flex-direction: column; align-items: center; justify-content: center; gap: 48px;
  }
  .card {
    width: 600px; height: 343px; border-radius: 18px; position: relative; overflow: hidden;
    box-shadow: 0 8px 24px rgba(0,0,0,0.18);
  }
  /* Back */
  .card--back { background: var(--card-dark); }
  .regional-mark {
    position: absolute; top: 48px; right: 40px;
    display: flex; align-items: center; gap: 10px;
    font-family: "Cinzel", serif; font-weight: 600; font-size: 17px; letter-spacing: 1px;
    color: var(--red);
  }
  .regional-mark .mark-square { width: 14px; height: 14px; background: var(--red); }
  .brand-mark {
    position: absolute; left: 56px; top: 150px;
    display: flex; align-items: center; gap: 16px;
    font-family: "Cinzel", serif; font-weight: 600; font-size: 46px; letter-spacing: 2px;
    color: var(--silver);
  }
  .brand-mark .mark-square { width: 40px; height: 40px; background: #3c3c3d; }
  /* Front */
  .card--front { background: var(--card-light); }
  .front-brand {
    position: absolute; top: 42px; right: 44px;
    display: flex; align-items: center; gap: 10px;
    font-family: "Cinzel", serif; font-weight: 600; font-size: 26px; letter-spacing: 1px;
    color: var(--ink);
  }
  .front-brand .mark-square { width: 22px; height: 22px; background: var(--ink); }
  .rule { position: absolute; left: 40px; right: 40px; height: 1px; background: var(--rule); }
  .rule--top { top: 150px; }
  .rule--bottom { top: 250px; }
  .person { position: absolute; left: 40px; top: 172px; font-family: "Cinzel", serif; color: var(--ink); }
  .person__name { font-size: 26px; letter-spacing: 1px; font-weight: 400; }
  .person__title { font-size: 16px; color: var(--ink-soft); margin-top: 2px; }
  .contacts {
    position: absolute; left: 40px; top: 266px;
    font-family: "Work Sans", sans-serif; font-size: 13px; line-height: 1.7; color: var(--ink-soft);
  }
  .contacts b { color: var(--ink); font-weight: 600; }
</style>
</head>
<body>
<main class="canvas">
  <section class="card card--back" aria-label="Card back">
    <div class="regional-mark"><span class="mark-square"></span>Moorfield Regional Center</div>
    <div class="brand-mark"><span class="mark-square"></span>Talvane Capital</div>
  </section>
  <section class="card card--front" aria-label="Card front">
    <div class="front-brand"><span class="mark-square"></span>Talvane Capital</div>
    <div class="rule rule--top"></div>
    <div class="person">
      <h1 class="person__name">Dorian Talvane</h1>
      <p class="person__title">CEO</p>
    </div>
    <div class="rule rule--bottom"></div>
    <div class="contacts">
      <p><b>C:</b> +1.555.318.4476 | <b>P:</b> +1.555.240.6185 | <b>M:</b> dtalvane@talvanecompanies.example</p>
      <p><b>W:</b> www.<b>talvanecompanies</b>.example</p>
    </div>
  </section>
</main>
</body>
</html>
```